Breezeway Comfort business cards design

Need a business card design for a Heating and Air Conditioning business. I need these items included.
Business name: Breezeway Comfort
Owner: Marcus Tollefsen
License # 2874590
Phone number # 555-382-4071
Email: breezewaycomfortair@mailvista.example
Sales
Service
Installation
Maintenance

Heating and Air Conditioning

Requirements
Must have
• Company name , license number , phone number , email

```html
<!DOCTYPE html>
<html lang="en">
<head>
<meta charset="utf-8">
<title>Breezeway Comfort – Business Cards</title>
<link rel="stylesheet" href="https://fonts.googleapis.com/css2?family=Poppins:wght@400;500;600&display=swap">
<style>
  :root{
    --bg:#2a2b2e;
    --paper:#ffffff;
    --brand-blue:#0a3ea8;
    --brand-orange:#f7842a;
    --brand-red:#ee4a3a;
    --brand-pink:#e3246b;
    --ink-grey:#6f6f73;
    --rule-grey:#9a9a9e;
  }
  *{box-sizing:border-box;margin:0;padding:0}
  html,body{width:1200px;height:952px;overflow:hidden}
  body{background:var(--bg);font-family:"Poppins",sans-serif;position:relative}

  .card{position:absolute;left:290px;width:620px;height:354px;border-radius:4px;overflow:hidden;box-shadow:0 10px 30px rgba(0,0,0,.45)}
  .card--front{top:84px;background:var(--paper)}
  .card--back{top:484px;background:var(--brand-blue)}

  /* front */
  .accent-line{position:absolute;left:32px;width:4px}
  .accent-line--blue{top:0;height:168px;background:var(--brand-blue)}
  .accent-line--warm{top:178px;height:176px;background:linear-gradient(to bottom,var(--brand-orange),var(--brand-red) 60%,var(--brand-pink))}

  .wordmark{position:absolute;display:flex;align-items:center;gap:10px;font-weight:600;letter-spacing:.04em;text-transform:uppercase}
  .wordmark__dot{width:12px;height:12px;border-radius:50%;background:var(--brand-orange)}
  .card--front .wordmark{left:64px;top:40px;font-size:24px;color:var(--brand-blue)}

  .contact{position:absolute;left:240px;top:132px}
  .contact__name{font-size:25px;font-weight:500;letter-spacing:.08em;text-transform:uppercase;line-height:1.1}
  .contact__first{color:var(--brand-blue)}
  .contact__last{color:var(--brand-orange);font-weight:600}
  .contact__title{font-size:14px;color:var(--ink-grey);margin-top:4px}
  .contact__rule{width:64px;height:1.5px;background:var(--rule-grey);margin:8px 0 12px}
  .contact__row{display:flex;align-items:center;gap:9px;font-size:13.5px;color:var(--ink-grey);margin-bottom:8px}
  .contact__icon{width:20px;height:20px;border-radius:4px;background:var(--brand-blue);display:flex;align-items:center;justify-content:center;flex:none}
  .license{position:absolute;left:216px;top:294px;font-size:14px;font-weight:500}
  .license__label{color:var(--brand-orange)}
  .license__number{color:var(--brand-blue)}

  /* back */
  .services{position:absolute;left:96px;top:34px;list-style:none;color:#fff;font-size:14px;line-height:26px}
  .services li{display:flex;align-items:center;gap:8px}
  .services li::before{content:"";width:5px;height:5px;border-radius:50%;background:var(--brand-red)}
  .card--back .wordmark{left:58px;top:186px;font-size:26px;color:#fff}
</style>
</head>
<body>

<section class="card card--front" aria-label="Business card front">
  <span class="accent-line accent-line--blue"></span>
  <span class="accent-line accent-line--warm"></span>

  <div class="wordmark"><span class="wordmark__dot"></span>Breezeway Comfort</div>

  <div class="contact">
    <h1 class="contact__name"><span class="contact__first">Marcus</span> <span class="contact__last">Tollefsen</span></h1>
    <p class="contact__title">Managing Director</p>
    <div class="contact__rule"></div>
    <p class="contact__row">
      <span class="contact__icon">
        <svg width="12" height="12" viewBox="0 0 24 24" aria-hidden="true"><path fill="#fff" d="M6.6 10.8a15.1 15.1 0 0 0 6.6 6.6l2.2-2.2c.3-.3.7-.4 1-.2 1.1.4 2.3.6 3.6.6.6 0 1 .4 1 1V20c0 .6-.4 1-1 1A17 17 0 0 1 3 4c0-.6.4-1 1-1h3.5c.6 0 1 .4 1 1 0 1.3.2 2.5.6 3.6.1.3 0 .7-.2 1z"/></svg>
      </span>555-382-4071
    </p>
    <p class="contact__row">
      <span class="contact__icon">
        <svg width="12" height="12" viewBox="0 0 24 24" aria-hidden="true"><rect x="2" y="5" width="20" height="14" rx="1.5" fill="none" stroke="#fff" stroke-width="2"/><path d="M2 6l10 7 10-7" fill="none" stroke="#fff" stroke-width="2"/></svg>
      </span>breezewaycomfortair@mailvista.example
    </p>
  </div>

  <p class="license"><span class="license__label">License</span> <span class="license__number"># 2874590</span></p>
</section>

<section class="card card--back" aria-label="Business card back">
  <ul class="services">
    <li>Sales</li>
    <li>Service</li>
    <li>Installation</li>
    <li>Maintenance</li>
  </ul>
  <div class="wordmark">Breezeway Comfort</div>
</section>

</body>
</html>
```